Two Rivers Lantern Press Book Cover for: "Growing Older Wisely"

We are a publishing company who plans to launch the book, Growing Older Wisely, A Simple Handy Manual for Planning, Money and Inner Balance in late 2018. We desire a book cover that creates interest, looks professional and can draw readers to open and purchase this book. Growing Older Wisely is an invaluable, self-help book which provides Generation X, Baby Boomers and their families with the following information: steps to obtain valid, reliable wills and trusts, identify and pay for health care, address end of life care and manage grief. (Please see the attached book description for more information about the book contents). The cover needs to have a "wellness", health and healing emphasis but it should not be morbid. Instead, the cover should have an uplifting, inviting and engaging feeling.

The designer should use Photoshop to develop the 5 x 7 cover. Please design the front, back cover and spine using the attached suggested layout as a guide. Use colors that complement the background colors in the author's photo and the logo for the front and back colors. Feel free to change the colors of the black rectangles on the front of the book. We are looking for a design to be added using the suggested layouts but we are open to modifications of the layout provided that all the content in the attachments are used. Below are the specifications needed for the cover:

-Use Photoshop
-Develop a front and back cover for a 5 x 7 format book
-Include the book title, subtitle and author name on the front cover as noted on the front cover attachment
-Include a book title and author names on the spine of the cover
-Use full bleed background if appropriate
-Color correct and resize images as necessary
-Insert logo and publisher’s imprint on spine and back cover as noted in attachments

For designers who are successful with this contest, we will primarily consider you for future projects.

Thanks!

Target Market(s)

Generation X, Baby Boomers and their families

Industry/Entity Type

Book Publisher

Font styles to use
Sans Serif

Colors

Designer to choose colors to be used in the design.

Requirements
Must have
• The designer should use Photoshop to develop the 5 x 7 cover. Please design the front, back cover and spine using the attached suggested layout as a guide. Use colors that complement the background colors in the author's photo and the logo for the front and back colors. Feel free to change the colors of the black rectangles on the front of the book. We are looking for a design to be added using the suggested layouts but we are open to modifications of the layout provided that all the content in the attachments are used. Below are the specifications needed for the cover:
• -Use Photoshop
• -Develop a front and back cover for a 5 x 7 format book
• -Include the book title, subtitle and author name on the front cover as noted on the front cover attachment
• -Include a book title and author names on the spine of the cover
• -Use full bleed background if appropriate
• -Color correct and resize images as necessary
• -Insert logo and publisher’s imprint on spine and back cover as noted in attachments
Nice to have
• N/A
Should not have
• The design should not specifically duplicate the layout samples or include pictures of persons on the cover. We have provided those as a guide; we are looking for innovation and professionalism.

```html
<!DOCTYPE html>
<html lang="en">
<head>
<meta charset="utf-8">
<title>Growing Older Wisely — Book Cover</title>
<link rel="stylesheet" href="https://fonts.googleapis.com/css2?family=Oswald:wght@400;500;600;700&family=Tinos:wght@400;700&display=swap">
<style>
  :root {
    --stage: #a6a6a6;
    --violet-deep: #3d3f8e;
    --violet-mid: #6d70c2;
    --violet-soft: #9fa3e0;
    --lavender: #c9cbf2;
    --spine: #4a4c98;
    --ink-navy: #1f2150;
    --author-tint: #dfe5ff;
    --white: #ffffff;
  }
  * { box-sizing: border-box; margin: 0; padding: 0; }
  html, body { width: 1200px; height: 906px; overflow: hidden; }
  body { background: var(--stage); position: relative; font-family: "Tinos", "Times New Roman", serif; color: var(--white); }

  .cover { position: absolute; left: 56px; top: 99px; width: 1095px; height: 710px; overflow: hidden; }

  .back, .spine, .front { position: absolute; top: 0; height: 100%; }
  .back { left: 0; width: 514px; }
  .spine { left: 514px; width: 44px; }
  .front { left: 558px; width: 537px; }

  .back-art { position: absolute; inset: 0;
    background:
      radial-gradient(ellipse at 30% 45%, rgba(201,203,242,.55), transparent 60%),
      radial-gradient(ellipse at 80% 80%, rgba(159,163,224,.5), transparent 55%),
      linear-gradient(180deg, var(--violet-deep) 0%, var(--violet-mid) 55%, var(--violet-soft) 100%); }
  .front-art { position: absolute; inset: 0;
    background:
      radial-gradient(ellipse at 75% 20%, rgba(201,203,242,.6), transparent 50%),
      radial-gradient(ellipse at 15% 75%, rgba(201,203,242,.45), transparent 45%),
      linear-gradient(180deg, var(--violet-mid) 0%, var(--violet-soft) 45%, var(--violet-mid) 100%); }
  .spine { background: linear-gradient(180deg, var(--spine), var(--violet-mid) 60%, var(--spine)); border-left: 1px solid rgba(255,255,255,.35); border-right: 1px solid rgba(255,255,255,.35); }

  /* back cover */
  .back-title { position: absolute; top: 52px; left: 0; width: 518px; text-align: center; font-size: 26px; font-weight: 700; letter-spacing: .5px; }
  .back-subtitle { position: absolute; top: 84px; left: 0; width: 518px; text-align: center; font-size: 19px; font-weight: 700; line-height: 23px; }
  .back-copy { position: absolute; top: 148px; left: 42px; width: 460px; font-size: 13.6px; line-height: 15px; text-align: justify; }
  .back-copy p + p { margin-top: 14px; }
  .bio { margin-top: 16px; text-align: left; }
  .bio strong { font-weight: 700; }
  .author-photo { float: left; width: 122px; height: 182px; margin: 50px 10px 0 8px;
    background: linear-gradient(180deg, #8d90d4 0%, #5b5fae 55%, #2b2d5c 100%); border-radius: 4px; }
  .isbn { position: absolute; top: 649px; left: 283px; font-family: "Oswald", Arial, sans-serif; font-size: 13px; font-weight: 400; }
  .isbn-box { position: absolute; top: 572px; left: 283px; width: 202px; height: 117px; background: var(--white); }
  .imprint { position: absolute; top: 604px; left: 28px; display: flex; align-items: center; gap: 8px; }
  .imprint-square { width: 18px; height: 18px; background: var(--white); }
  .imprint-name { font-family: "Oswald", Arial, sans-serif; font-size: 11px; line-height: 13px; text-transform: uppercase; letter-spacing: .5px; }
  .website { position: absolute; top: 674px; left: 78px; font-family: "Oswald", Arial, sans-serif; font-size: 14px; font-style: normal; }

  /* spine */
  .spine-titles { position: absolute; top: 14px; left: 0; width: 44px; height: 560px; writing-mode: vertical-rl; display: flex; align-items: center; }
  .spine-title { font-family: "Oswald", Arial, sans-serif; font-weight: 700; font-size: 20px; letter-spacing: 1px; line-height: 22px; }
  .spine-subtitle { font-size: 13px; line-height: 15px; }
  .spine-rule { position: absolute; left: 4px; width: 36px; height: 1px; background: var(--white); }
  .spine-authors { position: absolute; top: 594px; left: 0; width: 44px; text-align: center; font-family: "Oswald", Arial, sans-serif; font-size: 11px; line-height: 14px; }
  .spine-imprint { position: absolute; top: 672px; left: 0; width: 44px; display: flex; flex-direction: column; align-items: center; gap: 3px; font-family: "Oswald", Arial, sans-serif; font-size: 7px; }
  .spine-imprint span:first-child { width: 10px; height: 10px; background: var(--white); }

  /* front cover */
  .front-author { position: absolute; top: 58px; left: 98px; font-family: "Oswald", Arial, sans-serif; font-weight: 600; font-size: 16px; color: var(--author-tint); letter-spacing: .3px; }
  .front-title { font-family: "Oswald", Arial, sans-serif; font-weight: 700; color: var(--white); text-transform: uppercase; }
  .front-title span { position: absolute; font-size: 118px; line-height: 1; text-shadow: 0 2px 6px rgba(31,33,80,.25); }
  .title-1 { top: 190px; left: 56px; }
  .title-2 { top: 308px; left: 90px; letter-spacing: 26px; }
  .title-3 { top: 426px; left: 196px; }
  .front-subtitle { position: absolute; top: 580px; right: 28px; text-align: right; font-family: "Oswald", Arial, sans-serif; color: var(--ink-navy); font-weight: 600; line-height: 1.15; }
  .front-subtitle .line-1 { font-size: 22px; }
  .front-subtitle .line-1 b { font-size: 27px; font-weight: 700; }
  .front-subtitle .line-2 { font-size: 19px; }
</style>
</head>
<body>
  <main class="cover">
    <section class="back">
      <div class="back-art" role="img" aria-label="Soft violet photograph of dandelion seeds drifting, continued from the front"></div>
      <h2 class="back-title">Growing Older Wisely</h2>
      <p class="back-subtitle">A Simple Handy Manual for Planning,<br>Money and Inner Balance</p>
      <div class="back-copy">
        <p>Death and taxes may be inevitable, but they both require a lot of preparation. Fifty percent of America’s seventy-four million baby boomers have parents eighty or older, and nearly half of those boomers haven’t discussed end-of-life issues with their loved ones.</p>
        <p>In Growing Older Wisely, the authors present a detailed, step-by-step guide on how to deal with aging. They tackle issues such as wills and trusts, estate planning, senior housing, caregiving, hospice care, and death and bereavement. Their approach is lighthearted but thorough, and they provide a sorely needed examination of all the details involved in growing old in America.</p>
        <div class="bio">
          <p><strong>Renata L. Hale</strong> is a social services administrator, and Contributor Marcus J. Whitfield is an attorney. They have combined their skills and knowledge to give readers a practical understanding of the issues involved in caring for an elderly family member.</p>
          <div class="author-photo" role="img" aria-label="Author portrait"></div>
          <p>Renata L. Hale holds an advanced degree in Public Administration from Eastbrook State University and is currently an Administrator at the Westmoor County Office of Family Services.</p>
          <p>Collaborator Marcus J. Whitfield is an attorney who has practiced for thirty-five years in the areas of family law, wills, trusts, and estate planning. In Growing Older Wisely, the two have pooled their expertise to provide an invaluable guide to all the issues involved in caring for a loved one at the end of his or her life.</p>
        </div>
      </div>
      <div class="isbn-box" aria-hidden="true"></div>
      <p class="isbn" style="top:552px">ISBN: 978-1-000-00000-0</p>
      <div class="imprint">
        <span class="imprint-square"></span>
        <span class="imprint-name">Two Rivers Lantern Press</span>
      </div>
      <address class="website">www.renatahalewrites.com</address>
    </section>

    <section class="spine">
      <div class="spine-titles">
        <span class="spine-title">GROWING OLDER WISELY</span>
        <span class="spine-subtitle">A Simple Handy Manual for Planning, Money and Inner Balance</span>
      </div>
      <span class="spine-rule" style="top:580px"></span>
      <p class="spine-authors">HALE<br>with<br>WHITFIELD</p>
      <span class="spine-rule" style="top:650px"></span>
      <div class="spine-imprint"><span></span><span>TWO RIVERS</span></div>
    </section>

    <section class="front">
      <div class="front-art" role="img" aria-label="Soft-focus violet photograph of a dandelion releasing its seeds"></div>
      <p class="front-author">RENATA L. HALE, M.P.A. with MARCUS J. WHITFIELD, ESQ.</p>
      <h1 class="front-title">
        <span class="title-1">Growing</span>
        <span class="title-2">Older</span>
        <span class="title-3">Wisely</span>
      </h1>
      <p class="front-subtitle">
        <span class="line-1">A Simple Handy <b>MANUAL</b></span><br>
        <span class="line-2">for Planning, Money and Inner Balance</span>
      </p>
    </section>
  </main>
</body>
</html>
```